new business card and logo for a high end Automotive repair and performance shop

Need to update our design for our business cards. New address, and want a new look. I'll upload some pics of our current card. We are a high end auto repair/tuning shop. New address will be 5192 W. Larkfield Ave FERNWICK, T.X. 70123. I do have the vector files if needed. The logo would have a similar design. Love the look of carbon fiber, and brushed aluminum, although may have issues showing the texture of the material due to dpi restrictions during card printing. Also the logo would have to be easily printed on shirts, and for embroidery. Thanks, and good luck.

www.motor-zenith.example

Target Market(s)

High end automotive repair, dealership alternative.

Industry/Entity Type

Automotive

Contact Information for Business Card

MOTORZENITH
5192 W. LARKFIELD AVE
FERNWICK, T.X. 70123
PH 555-307-9261
FAX 555-307-4470
EMAIL INFO@MOTOR-ZENITH.EXAMPLE

Logo Text

MotorZenith

Font styles to use
Sans Serif

Requirements
Must have
• name, address, description that was uploaded.
Nice to have
• maybe some brands i.e. vardo, orvex, Talvani, qrt, solvanta, dovik etc. not necessary. simple is good, like the look of carbon fiber, brushed aluminum.
Should not have
• open to all suggestions.

```html
<!DOCTYPE html>
<html lang="en">
<head>
<meta charset="utf-8">
<title>MotorZenith Business Card</title>
<link href="https://fonts.googleapis.com/css2?family=Michroma&display=swap" rel="stylesheet">
<style>
  :root {
    --page-bg: #eeeeee;
    --band-black: #0d0d0d;
    --band-black-hi: #262626;
    --band-red: #5a0f12;
    --band-red-hi: #7a1a1e;
    --band-grey: #2e2e2e;
    --band-grey-hi: #4a4a4a;
    --accent-red: #ff1e1e;
    --text-light: #f2f2f2;
    --metal: #d6d6d6;
  }
  * { margin: 0; padding: 0; box-sizing: border-box; }
  html, body {
    width: 1200px;
    height: 901px;
    overflow: hidden;
    background: var(--page-bg);
  }
  .canvas {
    position: relative;
    width: 1200px;
    height: 901px;
    font-family: "Michroma", "Arial", sans-serif;
  }
  .card {
    position: absolute;
    width: 432px;
    height: 268px;
    display: grid;
    grid-template-rows: 22% 50% 28%;
    overflow: hidden;
    box-shadow: 4px 6px 10px rgba(0, 0, 0, 0.35);
  }
  .card--front { left: 236px; top: 200px; }
  .card--back  { left: 514px; top: 404px; }
  .band { width: 100%; height: 100%; }
  .band--top    { background: linear-gradient(180deg, var(--band-black-hi), var(--band-black)); }
  .band--middle {
    position: relative;
    background: linear-gradient(160deg, var(--band-red-hi), var(--band-red) 60%, #3e0a0c);
    box-shadow: inset 0 6px 10px rgba(0,0,0,0.5), inset 0 -6px 10px rgba(0,0,0,0.5);
  }
  .band--bottom { background: linear-gradient(180deg, var(--band-grey-hi), var(--band-grey)); }

  .brand-lockup {
    position: absolute;
    left: 50%;
    top: 50%;
    transform: translate(-50%, -50%);
    display: flex;
    align-items: center;
    gap: 10px;
  }
  .brand-lockup__dot {
    width: 14px;
    height: 14px;
    border-radius: 50%;
    background: var(--metal);
  }
  .brand-lockup__name {
    color: var(--metal);
    font-size: 21px;
    letter-spacing: 1px;
    white-space: nowrap;
  }

  .contact {
    position: absolute;
    left: 112px;
    top: 14px;
    list-style: none;
    font-size: 10px;
    line-height: 17px;
    letter-spacing: 0.5px;
    color: var(--text-light);
    white-space: nowrap;
  }
  .contact__name,
  .contact__email { color: var(--accent-red); }
</style>
</head>
<body>
<main class="canvas">
  <section class="card card--front" aria-label="Business card front">
    <div class="band band--top" role="img" aria-label="Black carbon fibre texture band"></div>
    <div class="band band--middle" role="img" aria-label="Dark red carbon fibre texture band with brand name">
      <div class="brand-lockup">
        <span class="brand-lockup__dot"></span>
        <span class="brand-lockup__name">MotorZenith</span>
      </div>
    </div>
    <div class="band band--bottom" role="img" aria-label="Grey carbon fibre texture band"></div>
  </section>

  <section class="card card--back" aria-label="Business card back">
    <div class="band band--top" role="img" aria-label="Black carbon fibre texture band"></div>
    <div class="band band--middle" role="img" aria-label="Dark red carbon fibre texture band with contact details">
      <ul class="contact">
        <li class="contact__name">MOTORZENITH</li>
        <li>5192 W. LARKFIELD AVE</li>
        <li>FERNWICK, T.X. 70123</li>
        <li>PH 555-307-9261</li>
        <li>FAX 555-307-4470</li>
        <li class="contact__email">EMAIL INFO@MOTOR-ZENITH.EXAMPLE</li>
      </ul>
    </div>
    <div class="band band--bottom" role="img" aria-label="Grey carbon fibre texture band"></div>
  </section>
</main>
</body>
</html>
```